Qb Panes

We need a website design for a company based in Texas that specializes in doors and and windows.
Qb Pane is a leading window manufacturer of aluminum and vinyl windows, both serving the replacement and new construction markets. Qb Pane Inc. was created over 25 years ago when two existing window manufacturers with excellent reputations in their fields - merged. Qb Pane offers a complete line conforming to the needs of residential and commercial window markets.
The final design should be something that communicates professionalism and features they're key value propositions.
Example websites we like:
http://layouts.pebblecraft.example/zx/satchel/
http://layouts.pebblecraft.example/zx/splashyard/
http://layouts.pebblecraft.example/zx/rebuildr2/
This design should format the existing content to be more visually organized, improve the fonts to clearer and more readable, and make it easier for users to find services.
Brand guide is attached
Website images can be found here: https://docs.vaultcrate.example/7kRTmwQzLpXeBd
Target Market(s)
Windows
Number of Pages Required
1 page
Look and feel
Each slider illustrates characteristics of the customer's brand and the style your logo design should communicate.

```html
<!DOCTYPE html>
<html lang="en">
<head>
<meta charset="utf-8">
<title>Qb Pane — Modern Windows & Doors</title>
<link rel="stylesheet" href="https://fonts.googleapis.com/css2?family=Raleway:ital,wght@0,400;0,500;0,600;0,700;1,400&display=swap">
<style>
:root{
  --maroon:#a3173a;
  --gold:#d5b24e;
  --ink:#2b2b2b;
  --muted:#555;
  --teal:#2f5a55;
  --grey-bg:#ededed;
  --white:#fff;
  --footer-line:#d9c58c;
}
*{box-sizing:border-box;margin:0;padding:0}
html,body{width:1200px;height:3429px;overflow:hidden}
body{font-family:"Raleway",sans-serif;color:var(--ink);background:var(--white);position:relative}
.abs{position:absolute}

/* top bar */
.topbar{left:0;top:0;width:1200px;height:41px;background:var(--maroon);color:var(--white);font-size:12px;display:flex;align-items:center;padding-left:41px}
.topbar strong{font-weight:700;font-size:13px;margin-right:34px}
.topbar .contact{display:flex;align-items:center;gap:10px;margin-right:36px}
.topbar svg{width:20px;height:20px}

/* nav */
.nav{left:0;top:41px;width:1200px;height:101px;background:var(--white);border-bottom:1px solid #ddd}
.brand{left:41px;top:28px;font-size:34px;font-weight:600;color:var(--maroon);display:flex;align-items:center;gap:10px;letter-spacing:.5px}
.brand .dot,.footer-brand .dot{width:14px;height:14px;border-radius:50%;background:var(--gold)}
.menu{left:464px;top:43px;font-size:13px;font-weight:500;color:var(--ink);letter-spacing:.3px}
.menu a{color:inherit;text-decoration:none;position:absolute;white-space:nowrap}
.menu .active::after{content:"";position:absolute;left:-14px;right:-14px;top:53px;height:5px;background:var(--maroon)}
.buy{left:1029px;top:32px;width:128px;height:37px;background:var(--gold);color:var(--white);font-size:13px;font-weight:600;display:flex;align-items:center;justify-content:center;letter-spacing:.5px}

/* hero */
.hero-photo{left:0;top:142px;width:1200px;height:621px;background:linear-gradient(100deg,#9a8474 0%,#b39079 12%,#6d809c 24%,#52637a 32%,#5d5f63 42%,#47484c 58%,#3a3b3f 78%,#55595d 100%)}
.hero-scrim{left:0;top:142px;width:1200px;height:621px;background:linear-gradient(180deg,rgba(0,0,0,.05) 0%,rgba(0,0,0,.15) 60%,rgba(46,74,30,.55) 100%)}
.hero-title{left:640px;top:304px;width:540px;text-align:center;color:var(--white);font-size:64px;font-weight:500;line-height:76px}
.hero-copy{left:649px;top:474px;width:512px;text-align:center;color:var(--white);font-size:15px;font-weight:600;line-height:20px}
.quote-btn{left:770px;top:567px;width:272px;height:43px;background:var(--maroon);color:var(--white);font-size:16px;font-weight:600;display:flex;align-items:center;justify-content:center}

/* featured */
.grey-band{left:0;top:763px;width:1200px;height:993px;background:var(--grey-bg)}
.featured{left:41px;top:677px;width:1118px;height:690px;background:var(--white);box-shadow:0 0 6px rgba(0,0,0,.08)}
.section-title{font-size:22px;font-weight:500;color:var(--maroon);text-align:center;letter-spacing:.5px}
.featured .section-title{position:absolute;left:0;top:28px;width:100%}
.card{position:absolute;top:82px;width:318px;text-align:center}
.card .photo{width:318px;height:313px}
.card h3{font-size:13px;font-weight:600;margin-top:24px;letter-spacing:.3px}
.card p,.service p{font-size:11px;line-height:16px;color:var(--muted);margin:40px auto 0;width:300px}
.outline-btn{display:inline-flex;align-items:center;justify-content:center;width:135px;height:30px;font-size:10px;letter-spacing:.5px;margin-top:20px}
.outline-btn.gold{border:1px solid var(--gold);color:var(--gold)}
.outline-btn.maroon{border:1px solid var(--maroon);color:var(--maroon)}
.arrow{position:absolute;width:20px;height:30px}

/* services */
.service{position:absolute;top:1345px;width:318px;text-align:center}
.service svg{width:156px;height:156px}
.service h3{font-size:13px;font-weight:600;margin-top:38px;letter-spacing:.3px}
.service p{margin-top:42px}

/* works */
.works-photo{top:1817px;height:416px}
.works-title{left:880px;top:1808px;width:279px;text-align:right;font-size:30px;font-weight:500;color:var(--maroon)}
.works-sub{left:880px;top:1862px;width:279px;text-align:right;font-size:14px;color:var(--maroon);letter-spacing:.5px}
.works-copy{left:880px;top:1910px;width:279px;text-align:right;font-size:13px;line-height:24px;color:var(--maroon)}
.view-all{left:1024px;top:2126px;width:135px;height:30px;border:1px solid var(--gold);color:var(--gold);font-size:11px;display:flex;align-items:center;justify-content:center;letter-spacing:.5px}

/* clients */
.clients{left:0;top:2290px;width:1200px;height:659px;background:linear-gradient(180deg,#3b4b68 0%,#56627a 30%,#6b6a6c 52%,#4a5240 72%,#33402c 100%)}
.clients .section-title{position:absolute;left:0;top:34px;width:100%;color:var(--white)}
.testimonial{position:absolute;top:186px;width:318px;height:317px;background:var(--white);text-align:center;padding-top:96px;box-shadow:0 2px 8px rgba(0,0,0,.25)}
.avatar{position:absolute;left:102px;top:-57px;width:114px;height:114px;border-radius:50%;border:5px solid var(--white)}
.testimonial h3{font-size:17px;font-weight:600;letter-spacing:.5px}
.testimonial .role{font-size:12px;font-style:italic;color:var(--muted);margin-top:6px}
.testimonial p{font-size:11px;font-style:italic;line-height:17px;color:var(--muted);width:286px;margin:20px auto 0}
.dots{position:absolute;left:516px;top:576px;display:flex;gap:14px}
.dots span{width:21px;height:21px;border-radius:50%;border:3px solid var(--white)}
.dots .on{background:var(--maroon);border-color:var(--maroon)}

/* footer */
.footer-brand{left:41px;top:3046px;font-size:34px;font-weight:600;color:var(--maroon);display:flex;align-items:center;gap:10px}
.footer-about{left:41px;top:3106px;width:245px;font-size:12px;line-height:19px;color:var(--ink)}
.footer-col{top:3058px;width:270px}
.footer-col h4{font-size:16px;font-weight:600;color:var(--ink);padding-bottom:10px;border-bottom:2px solid var(--footer-line)}
.footer-col ul{list-style:none;margin-top:18px}
.footer-col li{font-size:12px;line-height:27px}
.footer-col p{font-size:12px;line-height:19px;margin-top:18px}
.bottombar{left:0;top:3388px;width:1200px;height:41px;background:var(--maroon);color:var(--white);font-size:12px;font-weight:600;display:flex;align-items:center;justify-content:center}
</style>
</head>
<body>

<div class="abs topbar">
  <strong>Have a question?</strong>
  <span class="contact">
    <svg viewBox="0 0 24 24" fill="none" stroke="#fff" stroke-width="2"><path d="M5 3h4l2 5-3 2a11 11 0 0 0 6 6l2-3 5 2v4a2 2 0 0 1-2 2A17 17 0 0 1 3 5a2 2 0 0 1 2-2z"/></svg>
    +10 555 010 202
  </span>
  <span class="contact">
    <svg viewBox="0 0 24 24" fill="none" stroke="#fff" stroke-width="2"><rect x="2" y="5" width="20" height="14"/><path d="M2 5l10 8 10-8"/></svg>
    hello@qbpane.example
  </span>
</div>

<header class="abs nav">
  <div class="abs brand"><span class="dot"></span>Qb Pane</div>
  <nav class="abs menu">
    <a class="active" style="left:0">HOME</a>
    <a style="left:76px">WINDOWS</a>
    <a style="left:183px">DOORS</a>
    <a style="left:263px">IDEAS &amp; INSPIRATION</a>
    <a style="left:444px">CONTACT US</a>
  </nav>
  <div class="abs buy">BUY NOW</div>
</header>

<section>
  <div class="abs hero-photo" role="img" aria-label="Smiling couple seated in front of a modern dark brick house with large windows and a green lawn"></div>
  <div class="abs hero-scrim"></div>
  <h1 class="abs hero-title">Modern<br>Windows&amp; Doors</h1>
  <p class="abs hero-copy">Lorem Ipsum is simply dummy text of the printing and typesetting industry. Lorem Ipsum has been the industry's standard dummy text ever since the 1500s.</p>
  <div class="abs quote-btn">GET A QUOTE</div>
</section>

<div class="abs grey-band"></div>

<section class="abs featured">
  <h2 class="section-title">FEATURED WINDOW</h2>
  <svg class="arrow" style="left:4px;top:228px" viewBox="0 0 20 30"><path d="M14 6 6 15l8 9" fill="none" stroke="#e0cf9e" stroke-width="3"/></svg>
  <svg class="arrow" style="left:1094px;top:228px" viewBox="0 0 20 30"><path d="M6 6l8 9-8 9" fill="none" stroke="#e0cf9e" stroke-width="3"/></svg>
  <article class="card" style="left:48px">
    <div class="photo" role="img" aria-label="Bright cream kitchen with a window above the sink" style="background:linear-gradient(165deg,#f1ecdc 0%,#d9ccaa 30%,#c8b58c 55%,#9c7f52 80%,#6b5a44 100%)"></div>
    <h3>WINDOW NAME</h3>
    <p>Lorem Ipsum is simply dummy text of the printing and typesetting industry. Lorem Ipsum has been the industry's standard dummy text ever since the 1500s.</p>
    <span class="outline-btn gold">BROWSE MORE</span>
  </article>
  <article class="card" style="left:400px">
    <div class="photo" role="img" aria-label="Dining room with sliding glass doors opening to a deck" style="background:linear-gradient(180deg,#f4f4f2 0%,#cfd7de 25%,#8a9a7c 45%,#a47a5a 65%,#3a3632 85%,#5a4a3c 100%)"></div>
    <h3>WINDOW NAME</h3>
    <p>Lorem Ipsum is simply dummy text of the printing and typesetting industry. Lorem Ipsum has been the industry's standard dummy text ever since the 1500s.</p>
    <span class="outline-btn gold">BROWSE MORE</span>
  </article>
  <article class="card" style="left:752px">
    <div class="photo" role="img" aria-label="Kitchen with orange wood cabinets and a glazed door" style="background:linear-gradient(100deg,#e8dccb 0%,#d9a06a 25%,#c4622a 50%,#e3ddd2 70%,#b8501f 100%)"></div>
    <h3>WINDOW NAME</h3>
    <p>Lorem Ipsum is simply dummy text of the printing and typesetting industry. Lorem Ipsum has been the industry's standard dummy text ever since the 1500s.</p>
    <span class="outline-btn gold">BROWSE MORE</span>
  </article>
</section>

<section>
  <div class="service" style="left:89px">
    <svg viewBox="0 0 100 100" fill="none" stroke="var(--teal)" stroke-width="4" stroke-linecap="round">
      <path d="M50 26a22 22 0 0 0-13 40v8h26v-8a22 22 0 0 0-13-40z"/>
      <path d="M40 80h20M42 86h16M46 92h8M50 8v8M20 20l6 6M80 20l-6 6M10 48h8M82 48h8"/>
    </svg>
    <h3>INSPIRATION AND IDEAS</h3>
    <p>Lorem Ipsum is simply dummy text of the printing and typesetting industry. Lorem Ipsum has been the industry's standard dummy text ever since the 1500s.</p>
    <span class="outline-btn maroon">READ MORE</span>
  </div>
  <div class="service" style="left:441px">
    <svg viewBox="0 0 100 100" fill="none" stroke="var(--teal)" stroke-width="5">
      <rect x="14" y="10" width="72" height="80"/>
      <rect x="22" y="18" width="56" height="64"/>
      <path d="M50 18v64M22 50h56"/>
    </svg>
    <h3>WINDOWS</h3>
    <p>Lorem Ipsum is simply dummy text of the printing and typesetting industry. Lorem Ipsum has been the industry's standard dummy text ever since the 1500s.</p>
    <span class="outline-btn maroon">READ MORE</span>
  </div>
  <div class="service" style="left:793px">
    <svg viewBox="0 0 100 100" fill="var(--teal)">
      <path fill-rule="evenodd" d="M20 6h60v88H20zM26 12v76h21V12zM53 12v76h21V12z"/>
      <rect x="30" y="18" width="13" height="24"/><rect x="30" y="50" width="13" height="32"/>
      <rect x="57" y="18" width="13" height="24"/><rect x="57" y="50" width="13" height="32"/>
      <rect x="42" y="46" width="3" height="8" fill="#fff"/><rect x="55" y="46" width="3" height="8" fill="#fff"/>
    </svg>
    <h3>DOORS</h3>
    <p>Lorem Ipsum is simply dummy text of the printing and typesetting industry. Lorem Ipsum has been the industry's standard dummy text ever since the 1500s.</p>
    <span class="outline-btn maroon">READ MORE</span>
  </div>
</section>

<section>
  <div class="abs works-photo" style="left:41px;width:270px;background:linear-gradient(175deg,#9fb6d4 0%,#c4d2e2 18%,#5c5652 38%,#8a5e48 55%,#2e3032 75%,#4f6a34 100%)" role="img" aria-label="Brick house with a glazed sunroom extension"></div>
  <div class="abs works-photo" style="left:322px;width:270px;background:linear-gradient(180deg,#fbfbf8 0%,#e9ece4 30%,#a9bf8a 55%,#f1efe9 72%,#b36a4c 90%,#8a5a3e 100%)" role="img" aria-label="Bright room with white framed French doors opening to a garden"></div>
  <div class="abs works-photo" style="left:606px;width:270px;background:linear-gradient(90deg,#6f8e3e 0%,#a4c06a 35%,#d9d6c6 55%,#f2efe6 75%,#b8ac8e 100%)" role="img" aria-label="Sunroom with large windows overlooking green trees"></div>
  <h2 class="abs works-title">OUR WORKS</h2>
  <div class="abs works-sub">LOREM IPSUM</div>
  <p class="abs works-copy">Lorem Ipsum is simply dummy text of the printing and typesetting industry. Lorem Ipsum has been the industry's standard dummy text ever since the 1500s, when an unknown printer took a galley of type and scrambled it to make a type specimen book.</p>
  <div class="abs view-all">VIEW ALL</div>
</section>

<section class="abs clients" role="img" aria-label="Evening view of a large suburban house with trees">
  <h2 class="section-title">OUR CLIENTS SAY</h2>
  <svg class="arrow" style="left:40px;top:330px" viewBox="0 0 20 30"><path d="M14 6 6 15l8 9" fill="none" stroke="#fff" stroke-width="3"/></svg>
  <svg class="arrow" style="left:1140px;top:330px" viewBox="0 0 20 30"><path d="M6 6l8 9-8 9" fill="none" stroke="#fff" stroke-width="3"/></svg>
  <article class="testimonial" style="left:89px">
    <div class="avatar" role="img" aria-label="Portrait of John Doe" style="background:linear-gradient(180deg,#f3f3f3 0%,#d9b59a 45%,#3c3c44 100%)"></div>
    <h3>JOHN DOE</h3>
    <div class="role">Company CEO</div>
    <p>Lorem Ipsum is simply dummy text of the printing and typesetting industry. Lorem Ipsum has been the industry's standard dummy text ever since the 1500s, when an unknown printer took a galley of type and scrambled it to make a type specimen book. It has survived not only five centuries.</p>
  </article>
  <article class="testimonial" style="left:441px">
    <div class="avatar" role="img" aria-label="Portrait of Jay Doe" style="background:linear-gradient(180deg,#e9e9e9 0%,#cfab92 45%,#2c2e36 100%)"></div>
    <h3>JAY DOE</h3>
    <div class="role">Executive Director</div>
    <p>Lorem Ipsum is simply dummy text of the printing and typesetting industry. Lorem Ipsum has been the industry's standard dummy text ever since the 1500s, when an unknown printer took a galley of type and scrambled it to make a type specimen book. It has survived not only five centuries.</p>
  </article>
  <article class="testimonial" style="left:793px">
    <div class="avatar" role="img" aria-label="Portrait of Jane Doe" style="background:linear-gradient(180deg,#efe6dc 0%,#b77a48 40%,#e2b99c 70%,#7a5a48 100%)"></div>
    <h3>JANE DOE</h3>
    <div class="role">Marketing Manager</div>
    <p>Lorem Ipsum is simply dummy text of the printing and typesetting industry. Lorem Ipsum has been the industry's standard dummy text ever since the 1500s, when an unknown printer took a galley of type and scrambled it to make a type specimen book. It has survived not only five centuries.</p>
  </article>
  <div class="dots"><span></span><span></span><span class="on"></span><span></span><span></span></div>
</section>

<footer>
  <div class="abs footer-brand"><span class="dot"></span>Qb Pane</div>
  <p class="abs footer-about">Lorem Ipsum is simply dummy text of the printing and typesetting industry. Lorem Ipsum has been the industry's standard dummy text ever since the 1500s, when an unknown printer took a galley of type and scrambled it to make a type specimen book. It has survived not only five centuries.</p>
  <div class="abs footer-col" style="left:325px">
    <h4>Short Links</h4>
    <ul><li>Home</li><li>Windows</li><li>Doors</li><li>Ideas &amp; Inspiration</li><li>Contact Us</li></ul>
  </div>
  <div class="abs footer-col" style="left:606px">
    <h4>Our mission</h4>
    <p>Lorem Ipsum is simply dummy text of the printing and typesetting industry. Lorem Ipsum has been the industry's standard dummy text ever since the 1500s, when an unknown printer took a galley of type and scrambled it to make a type specimen book. It has survived not only five centuries.</p>
  </div>
  <div class="abs footer-col" style="left:889px">
    <h4>About us</h4>
    <ul><li>Lorem Ipsum</li><li>Lorem Ipsum</li><li>Lorem Ipsum</li><li>Lorem Ipsum</li><li>Lorem Ipsum</li><li>Lorem Ipsum</li></ul>
  </div>
  <div class="abs bottombar">© 2018 Qb Pane. All Rights Reserved</div>
</footer>

</body>
</html>
```